Illustration Design Project

I have an existing illustration I have written up, I need it professionally redone, perhaps as an infographic or new design from the current layout.

Pls plan for a few edits and revisions.

I will need it large enough to be made into a wall poster size.

```html
<!DOCTYPE html>
<html lang="en">
<head>
<meta charset="utf-8">
<title>Accountable vs. Complacency</title>
<link rel="stylesheet" href="https://fonts.googleapis.com/css2?family=Cinzel:wght@400;700&family=Patrick+Hand&family=Arimo:ital@1&display=swap">
<style>
  :root {
    --frame-dark: #141210;
    --frame-gold: #8a6a2e;
    --parchment-light: #f3dfa4;
    --parchment-mid: #e2b968;
    --parchment-deep: #c98a3a;
    --ink: #3b2a12;
    --arrow: #ec8a43;
    --badge-light: #fff4e8;
    --badge-orange: #f08a3c;
    --oval-ring: #1a1918;
    --oval-light: #eef0e4;
    --oval-dark: #4d5246;
    --title-white: #ffffff;
  }
  html, body {
    margin: 0;
    padding: 0;
    overflow: hidden;
    background: var(--frame-dark);
  }
  .poster {
    width: 900px;
    height: 1200px;
    position: relative;
    overflow: hidden;
  }
  .poster svg { display: block; }
  .kicker {
    font-family: 'Arimo', sans-serif;
    font-style: italic;
    font-size: 11px;
    fill: #1a1a1a;
  }
  .pole-title {
    font-family: 'Cinzel', serif;
    font-size: 42px;
    fill: var(--ink);
    letter-spacing: 1px;
  }
  .step-label {
    font-family: 'Cinzel', serif;
    font-size: 21px;
    fill: var(--ink);
    letter-spacing: 0.5px;
  }
  .step-quote {
    font-family: 'Patrick Hand', cursive;
    font-size: 18px;
    fill: var(--ink);
    letter-spacing: 0.5px;
  }
  .step-number {
    font-family: 'Cinzel', serif;
    font-weight: 700;
    font-size: 30px;
    fill: #1b1410;
  }
  .hub-title {
    font-family: 'Cinzel', serif;
    font-size: 52px;
    fill: var(--title-white);
    stroke: #2a2a26;
    stroke-width: 1;
  }
  .flow-line {
    fill: none;
    stroke: var(--arrow);
    stroke-linecap: round;
  }
</style>
</head>
<body>
<div class="poster">
<svg width="900" height="1200" viewBox="0 0 900 1200" xmlns="http://www.w3.org/2000/svg">
  <defs>
    <linearGradient id="frameTone" x1="0" y1="0" x2="1" y2="1">
      <stop offset="0" stop-color="#1c1812"/>
      <stop offset="0.5" stop-color="#2a2114"/>
      <stop offset="1" stop-color="#1c1812"/>
    </linearGradient>
    <radialGradient id="parchment" cx="0.45" cy="0.35" r="0.75">
      <stop offset="0" stop-color="var(--parchment-light)"/>
      <stop offset="0.55" stop-color="var(--parchment-mid)"/>
      <stop offset="1" stop-color="var(--parchment-deep)"/>
    </radialGradient>
    <radialGradient id="badge" cx="0.4" cy="0.3" r="0.8">
      <stop offset="0" stop-color="var(--badge-light)"/>
      <stop offset="0.45" stop-color="#ffd2ad"/>
      <stop offset="1" stop-color="var(--badge-orange)"/>
    </radialGradient>
    <radialGradient id="hubFill" cx="0.5" cy="0.45" r="0.6">
      <stop offset="0" stop-color="var(--oval-light)"/>
      <stop offset="0.6" stop-color="#a9ad9c"/>
      <stop offset="1" stop-color="var(--oval-dark)"/>
    </radialGradient>
    <marker id="arrowHead" viewBox="0 0 10 10" refX="3" refY="5" markerWidth="4.2" markerHeight="4.2" orient="auto">
      <path d="M0,0 L10,5 L0,10 z" fill="var(--arrow)"/>
    </marker>
  </defs>

  <!-- frame -->
  <rect class="frame-scrollwork" x="0" y="0" width="900" height="1200" fill="url(#frameTone)"
        role="img" aria-label="Ornamental black and gold scrollwork frame around the poster"/>
  <rect x="6" y="6" width="888" height="1188" fill="none" stroke="var(--frame-gold)" stroke-width="2"/>

  <!-- parchment field -->
  <ellipse class="parchment" cx="450" cy="612" rx="438" ry="588" fill="url(#parchment)"/>

  <!-- header -->
  <text class="kicker" x="450" y="54" text-anchor="middle">Accountable vs. Complacency</text>
  <text class="pole-title" x="450" y="106" text-anchor="middle">ACCOUNTABLE</text>
  <line x1="309" y1="113" x2="591" y2="113" stroke="var(--ink)" stroke-width="1.5"/>

  <!-- flow arrows -->
  <path class="flow-line" stroke-width="11" marker-end="url(#arrowHead)"
        d="M448,522 C444,470 446,420 452,370 C458,310 460,240 460,140"/>
  <path class="flow-line" stroke-width="11" marker-end="url(#arrowHead)"
        d="M455,690 C456,760 444,820 452,880 C458,940 463,990 463,1052"/>
  <path class="flow-line" stroke-width="12" marker-end="url(#arrowHead)"
        d="M286,96 C150,230 130,460 216,552"/>
  <path class="flow-line" stroke-width="12" marker-end="url(#arrowHead)"
        d="M560,1122 C730,1040 790,820 710,640"/>

  <!-- accountable ladder -->
  <g class="ladder ladder-up">
    <text class="step-label" x="428" y="218" text-anchor="end">GETS ON WITH IT</text>
    <circle cx="458" cy="211" r="23" fill="url(#badge)" stroke="#fff" stroke-width="1.5"/>
    <text class="step-number" x="458" y="222" text-anchor="middle">5</text>
    <text class="step-quote" x="487" y="217">“ O.K. ,let’s do it ! ”</text>

    <text class="step-label" x="426" y="282" text-anchor="end">FINS SOLUTION</text>
    <circle cx="458" cy="275" r="23" fill="url(#badge)" stroke="#fff" stroke-width="1.5"/>
    <text class="step-number" x="458" y="286" text-anchor="middle">4</text>
    <text class="step-quote" x="487" y="281">“ What can I do ? ”</text>

    <text class="step-label" x="418" y="348" text-anchor="end">OWNS IT</text>
    <circle cx="449" cy="341" r="23" fill="url(#badge)" stroke="#fff" stroke-width="1.5"/>
    <text class="step-number" x="449" y="352" text-anchor="middle">3</text>
    <text class="step-quote" x="478" y="347">“ If it’s to be, it’s up to me ! ”</text>

    <text class="step-label" x="409" y="408" text-anchor="end">ACKNOWLEDGES</text>
    <text class="step-label" x="409" y="434" text-anchor="end">REALITY</text>
    <circle cx="442" cy="403" r="23" fill="url(#badge)" stroke="#fff" stroke-width="1.5"/>
    <text class="step-number" x="442" y="414" text-anchor="middle">2</text>
    <text class="step-quote" x="472" y="407">“ This is the way it is. ”</text>

    <text class="step-label" x="416" y="472" text-anchor="end">SEEKS REALITY</text>
    <circle cx="448" cy="464" r="23" fill="url(#badge)" stroke="#fff" stroke-width="1.5"/>
    <text class="step-number" x="448" y="475" text-anchor="middle">1</text>
    <text class="step-quote" x="478" y="469">“ What’s happening ? ”</text>
  </g>

  <!-- hub -->
  <g class="hub">
    <ellipse cx="450" cy="603" rx="193" ry="84" fill="var(--oval-ring)"/>
    <ellipse cx="450" cy="603" rx="173" ry="68" fill="url(#hubFill)"
             role="img" aria-label="Soft grey oval panel with faint swirl decoration"/>
    <text class="hub-title" x="450" y="596" text-anchor="middle">LIFE</text>
    <text class="hub-title" x="450" y="648" text-anchor="middle">HAPPENS</text>
  </g>

  <!-- victim ladder -->
  <g class="ladder ladder-down">
    <text class="step-label" x="424" y="750" text-anchor="end">AVOIDS REALITY</text>
    <circle cx="455" cy="743" r="23" fill="url(#badge)" stroke="#fff" stroke-width="1.5"/>
    <text class="step-number" x="455" y="754" text-anchor="middle">1</text>
    <text class="step-quote" x="484" y="748">“ Ask no questions. ”</text>

    <text class="step-label" x="415" y="818" text-anchor="end">FIGHTS REALITY</text>
    <circle cx="446" cy="810" r="23" fill="url(#badge)" stroke="#fff" stroke-width="1.5"/>
    <text class="step-number" x="446" y="821" text-anchor="middle">2</text>
    <text class="step-quote" x="475" y="817">“ That’s not how I see it. ”</text>

    <text class="step-label" x="420" y="883" text-anchor="end">BLAMES</text>
    <circle cx="453" cy="876" r="23" fill="url(#badge)" stroke="#fff" stroke-width="1.5"/>
    <text class="step-number" x="453" y="887" text-anchor="middle">3</text>
    <text class="step-quote" x="482" y="878">“ If everyone would just</text>
    <text class="step-quote" x="495" y="900">do their job ! ”</text>

    <text class="step-label" x="424" y="938" text-anchor="end">PERSONAL</text>
    <text class="step-label" x="402" y="965" text-anchor="end">EXCUSES</text>
    <circle cx="461" cy="932" r="23" fill="url(#badge)" stroke="#fff" stroke-width="1.5"/>
    <text class="step-number" x="461" y="943" text-anchor="middle">4</text>
    <text class="step-quote" x="490" y="935">“ It’s not my job. ”</text>

    <text class="step-label" x="428" y="1004" text-anchor="end">WAITS : HOPES</text>
    <circle cx="463" cy="998" r="23" fill="url(#badge)" stroke="#fff" stroke-width="1.5"/>
    <text class="step-number" x="463" y="1009" text-anchor="middle">5</text>
    <text class="step-quote" x="494" y="1002">“ If it was meant to be,</text>
    <text class="step-quote" x="507" y="1024">it’ll happen. ”</text>
  </g>

  <!-- footer pole -->
  <text class="pole-title" x="453" y="1133" text-anchor="middle">VICTIM</text>
  <line x1="366" y1="1140" x2="540" y2="1140" stroke="var(--ink)" stroke-width="1.5"/>
</svg>
</div>
</body>
</html>
```